Verpackungen
Danke für die unkomplizierte Abwicklung!
Zielgruppe
Wir sind ein Lebensmittelhersteller und wollen eine neue Gewürzlinie für hochwertige Gewürze launchen. Hierbei handelt es sich um Gewürze für den Bereich Grillen und Kochen. Unsere Zielgruppe sind Männer sowie Frauen über 20 Jahre. Das Produkt selber soll sehr hochwertig sein, somit soll auch das Design den Premium-Aspekt widerspiegeln.
Die Markenbezeichnung lautet 'Kern & Rauch'.
Aufgabenstellung
Bei dem Projekt handelt es sich um eine Karton Umverpackung (Sekundärverpackung) mit jeweils 4 Runddosen (Primärverpackung)! Die Stanzkontur hängt dem Briefing an.
In der Verpackung sollen 'Mischungen würzender Zutaten' verpackt werden.
Es handelt sich bei der Verpackung um einen Fefco 427 Karton in braun (Kraft) mit EINFARBIGEM Druck auf der Außenseite.
Logodateien sind bereits vorhanden.
Aktuell gibt es 4 verschiedene BBQ Gewürze, die in dem Geschenkset kombiniert werden. Die Bezeichnungen sind:
Donnerkeil, Silberfuchs, Seemannsgold und Herbstfeuer. Das Design der Runddosen ist dem Briefing zu entnehmen.
WICHTIGER HINWEIS: Wir haben uns für den braunen und eher unscheinbaren Karton mit einfarbigem Druck entschieden um den Kontrasteffekt beim Öffnen zu verstärken.
Das Design soll einfach aber schick sein. Gerne dürfen Batches verwendet werden (aber kein Muss) wie z.B. 'liebevoll handgemacht', 'schonend verarbeitet', 'regional hergestellt'.
Auf die Verpackung müssen zusätzlich noch folgende Informationen:
1. Mischung würzender Zutaten
2. 4 x 50 g netto
3. Mindestens haltbar bis / Lot Nr.:
4. Recycling Symbol
5. EAN Code
6. KüVeTa GmbH & Co. KG, Lindenhainstr. 12, 84163 Talhausen
Für den EAN Code bitte vorerst einen Platzhalter / Dummy verwenden, der tatsächliche EAN Code wird vor der Dateiübergabe gesendet.

```html
<!DOCTYPE html>
<html lang="de">
<head>
<meta charset="utf-8">
<title>Kern &amp; Rauch – Umverpackung</title>
<link rel="stylesheet" href="https://fonts.googleapis.com/css2?family=Oswald:wght@400;600;700&display=swap">
<style>
  :root {
    --paper: #ffffff;
    --kraft: #c89a63;
    --kraft-line: #3a2a1a;
    --ink: #1e1a17;
    --ink-soft: rgba(30, 26, 23, 0.14);
  }
  * { margin: 0; padding: 0; box-sizing: border-box; }
  html, body { width: 1200px; height: 900px; overflow: hidden; background: var(--paper); }
  body { font-family: "Oswald", sans-serif; color: var(--ink); position: relative; }

  .panel {
    position: absolute;
    left: 180px;
    width: 840px;
    background-color: var(--kraft);
    overflow: hidden;
  }
  .pinstripes {
    background-image: repeating-linear-gradient(to bottom,
      transparent 0 13px, var(--kraft-line) 13px 14.2px);
  }

  /* Lid */
  .lid { top: 90px; height: 440px; }
  .lid .band {
    position: absolute; left: 0; top: 0; bottom: 0; width: 44px;
    background: var(--ink);
  }
  .vertical-label {
    position: absolute; white-space: nowrap;
    transform: rotate(-90deg); transform-origin: left top;
    text-transform: uppercase; letter-spacing: 0.06em;
  }
  .net-weight { left: 12px; top: 270px; color: var(--kraft); font-size: 15px; font-weight: 600; }
  .best-before { left: 58px; top: 300px; font-size: 14px; font-weight: 600; background: var(--kraft); padding: 0 6px; }

  .tin {
    position: absolute; width: 180px; height: 180px; border-radius: 50%;
    background: var(--ink); display: flex; align-items: center; justify-content: center;
    color: var(--kraft); font-weight: 700; font-size: 20px; letter-spacing: 0.08em;
    text-transform: uppercase;
  }
  .tin--silberfuchs  { left: 250px; top: 30px; }
  .tin--donnerkeil   { left: 150px; top: 220px; }
  .tin--seemannsgold { left: 600px; top: 60px; }
  .tin--herbstfeuer  { left: 500px; top: 235px; }

  .lid-center {
    position: absolute; left: 330px; top: 150px; width: 280px; height: 120px;
    background: var(--kraft); text-align: center; padding-top: 14px;
  }
  .sketch {
    position: absolute; inset: 0;
    background: radial-gradient(ellipse at center, var(--ink-soft), transparent 70%);
  }
  .brand { position: relative; font-size: 44px; font-weight: 400; line-height: 1.1; }
  .contents { position: relative; font-size: 15px; font-weight: 600; text-transform: uppercase; letter-spacing: 0.06em; }

  /* Front side */
  .front { top: 560px; height: 230px; }
  .front .band { position: absolute; left: 0; top: 0; bottom: 0; width: 44px; background: var(--ink); }
  .front .edge-stripes { position: absolute; right: 0; top: 0; bottom: 0; width: 60px; }
  .recycle { position: absolute; left: 80px; top: 60px; width: 40px; height: 40px; }
  .front-copy { position: absolute; left: 220px; right: 120px; top: 28px; text-align: center; }
  .front-copy .brand { font-size: 50px; }
  .front-copy .contents { font-size: 18px; }
  .address { font-size: 15px; text-transform: uppercase; letter-spacing: 0.04em; line-height: 1.35; margin-top: 6px; }
</style>
</head>
<body>
  <section class="panel lid pinstripes" aria-label="Deckel">
    <div class="band"></div>
    <div class="vertical-label net-weight">4 x 50 g netto</div>
    <div class="vertical-label best-before">Mindestens haltbar bis / Lot Nr.:</div>

    <div class="tin tin--silberfuchs">Silberfuchs</div>
    <div class="tin tin--donnerkeil">Donnerkeil</div>
    <div class="tin tin--seemannsgold">Seemannsgold</div>
    <div class="tin tin--herbstfeuer">Herbstfeuer</div>

    <div class="lid-center">
      <div class="sketch" role="img" aria-label="Feine Strichzeichnung von Gewürzen hinter dem Markennamen"></div>
      <div class="brand">Kern &amp; Rauch</div>
      <div class="contents">Mischung würzender Zutaten</div>
    </div>
  </section>

  <section class="panel front" aria-label="Seitenfläche">
    <div class="band"></div>
    <div class="edge-stripes pinstripes"></div>
    <svg class="recycle" viewBox="0 0 40 40" aria-label="Recycling-Symbol" role="img">
      <g fill="none" stroke="#1e1a17" stroke-width="3.2" stroke-linecap="round" stroke-linejoin="round">
        <path d="M16 8 L20 3 L24 8 M20 3 L27 15"/>
        <path d="M33 24 L35 31 L28 32 M35 31 L22 31"/>
        <path d="M10 33 L4 28 L9 23 M4 28 L11 16"/>
      </g>
    </svg>
    <div class="front-copy">
      <div class="brand">Kern &amp; Rauch</div>
      <div class="contents">Mischung würzender Zutaten</div>
      <div class="address">KüVeTa GmbH &amp; Co. KG, Lindenhainstr. 12<br>84163 Talhausen</div>
    </div>
  </section>
</body>
</html>
```